Business Image

I have recently had a new company logo made up and require some new business cards to go with it.

Target Market(s)

Developers & high worth clients.

Industry/Entity Type

Business

Contact Information for Business Card

The business is in the construction/management industry. It needs to be classy but have a industrial feel. I would like the business card to be a elegant presentation in itself.

Requirements
Must have
• Current logo & company name. Colouring needs to be the same as the current design also.
Nice to have
• A few different designs & presentations of single and double sided business cards.

```html
<!DOCTYPE html>
<html lang="en">
<head>
<meta charset="utf-8">
<title>Meridian Build Group – Business Cards</title>
<link rel="stylesheet" href="https://fonts.googleapis.com/css2?family=Arimo:wght@400;700&display=swap">
<style>
  :root {
    --page: #e9e5df;
    --brand-blue: #2b6187;
    --ink-dark: #3a3d42;
    --card-white: #ffffff;
    --rule-grey: #4a4d52;
  }
  * { margin: 0; padding: 0; box-sizing: border-box; }
  html, body {
    width: 1200px; height: 1200px; overflow: hidden;
    background: var(--page);
    font-family: "Arimo", Arial, sans-serif;
  }
  .sheet {
    position: relative; width: 1200px; height: 1200px;
  }
  .card {
    position: absolute; left: 150px; width: 900px; height: 514px;
    box-shadow: 0 14px 30px rgba(0,0,0,0.18);
  }
  /* Back side */
  .card-back {
    top: 56px; background: var(--brand-blue);
    display: flex; align-items: center; justify-content: center;
  }
  .wordmark {
    display: flex; align-items: center; gap: 22px;
    font-weight: 700; letter-spacing: 0.04em; line-height: 1.05;
  }
  .wordmark-square { flex: none; }
  .wordmark-back { color: var(--card-white); }
  .wordmark-back .wordmark-square { width: 70px; height: 70px; border: 5px solid var(--card-white); }
  .wordmark-back .wordmark-name { font-size: 56px; }
  .wordmark-back .wordmark-sub { font-size: 25px; letter-spacing: 0.2em; }

  /* Front side */
  .card-front {
    top: 630px; background: var(--card-white); overflow: hidden;
  }
  .front-band {
    position: absolute; left: 0; right: 0; bottom: 0; height: 22px;
    background: var(--brand-blue);
  }
  .front-logo {
    position: absolute; left: 40px; top: 0; width: 380px; height: 492px;
    display: flex; align-items: center; justify-content: center;
  }
  .wordmark-front { color: var(--brand-blue); gap: 14px; }
  .wordmark-front .wordmark-square { width: 42px; height: 42px; background: var(--brand-blue); }
  .wordmark-front .wordmark-name { font-size: 38px; }
  .wordmark-front .wordmark-sub { font-size: 16px; letter-spacing: 0.16em; }
  .front-divider {
    position: absolute; left: 450px; top: 150px; width: 3px; height: 200px;
    background: var(--rule-grey);
  }
  .contact {
    position: absolute; left: 500px; top: 118px; color: var(--brand-blue);
  }
  .contact-name { font-size: 42px; font-weight: 400; line-height: 1.1; }
  .contact-role { font-size: 22px; color: var(--ink-dark); margin-bottom: 10px; }
  .contact-list { list-style: none; font-size: 22px; line-height: 1.35; }
  .contact-list li { display: flex; align-items: flex-start; gap: 12px; }
  .contact-icon { width: 18px; height: 18px; flex: none; margin-top: 4px; fill: var(--ink-dark); }
</style>
</head>
<body>
<main class="sheet">

  <section class="card card-back" aria-label="Business card back">
    <div class="wordmark wordmark-back">
      <span class="wordmark-square"></span>
      <div>
        <div class="wordmark-name">MERIDIAN</div>
        <div class="wordmark-sub">BUILD GROUP</div>
      </div>
    </div>
  </section>

  <section class="card card-front" aria-label="Business card front">
    <div class="front-logo">
      <div class="wordmark wordmark-front">
        <span class="wordmark-square"></span>
        <div>
          <div class="wordmark-name">MERIDIAN</div>
          <div class="wordmark-sub">BUILD GROUP</div>
        </div>
      </div>
    </div>

    <div class="front-divider"></div>

    <div class="contact">
      <div class="contact-name">Your Name</div>
      <div class="contact-role">CEO</div>
      <ul class="contact-list">
        <li>
          <svg class="contact-icon" viewBox="0 0 24 24" aria-hidden="true"><path d="M12 2a7 7 0 0 0-7 7c0 5 7 13 7 13s7-8 7-13a7 7 0 0 0-7-7zm0 9.5A2.5 2.5 0 1 1 12 6.5a2.5 2.5 0 0 1 0 5z"/></svg>
          <span>Full Address, FA 01<br>City Country</span>
        </li>
        <li>
          <svg class="contact-icon" viewBox="0 0 24 24" aria-hidden="true"><path d="M6.6 10.8a15 15 0 0 0 6.6 6.6l2.2-2.2a1 1 0 0 1 1-.25 11.4 11.4 0 0 0 3.6.6 1 1 0 0 1 1 1V20a1 1 0 0 1-1 1A17 17 0 0 1 3 4a1 1 0 0 1 1-1h3.5a1 1 0 0 1 1 1c0 1.25.2 2.45.6 3.6a1 1 0 0 1-.25 1z"/></svg>
          <span>0123 456 789</span>
        </li>
        <li>
          <svg class="contact-icon" viewBox="0 0 24 24" aria-hidden="true"><path d="M2 5h20v14H2zm2 2v.5l8 5 8-5V7zm0 2.8V17h16V9.8l-8 5z"/></svg>
          <span>info@yourbusiness.com</span>
        </li>
        <li>
          <svg class="contact-icon" viewBox="0 0 24 24" aria-hidden="true"><path d="M12 2a10 10 0 1 0 0 20 10 10 0 0 0 0-20zm6.9 6h-3a15 15 0 0 0-1.3-3.9A8 8 0 0 1 18.9 8zM12 4c.8 1.2 1.5 2.5 1.9 4h-3.8c.4-1.5 1.1-2.8 1.9-4zM4.3 14a8 8 0 0 1 0-4h3.4a16 16 0 0 0 0 4zm.8 2h3a15 15 0 0 0 1.3 3.9A8 8 0 0 1 5.1 16zm3-8h-3a8 8 0 0 1 4.3-3.9A15 15 0 0 0 8.1 8zM12 20c-.8-1.2-1.5-2.5-1.9-4h3.8c-.4 1.5-1.1 2.8-1.9 4zm2.3-6H9.7a14 14 0 0 1 0-4h4.6a14 14 0 0 1 0 4zm.3 5.9a15 15 0 0 0 1.3-3.9h3a8 8 0 0 1-4.3 3.9zm1.7-5.9a16 16 0 0 0 0-4h3.4a8 8 0 0 1 0 4z"/></svg>
          <span>www.yourbusiness.com</span>
        </li>
      </ul>
    </div>

    <div class="front-band"></div>
  </section>

</main>
</body>
</html>
```